Business cards for KORU Real Estate Holdings LLC

We need a cool, original business card design for a company based in the Washington DC metropolitan area. We are a new energetic and passionate Real Estate Investing Company that invests in all types of real estate; commercial, residential, industrial etc.

Our company color is Red since it reflects action, energy and speed; it is assertive confident, energizing, exciting, powerful, passionate and determined. So we would like business card communicate those qualities to the audience.

Our audiences are investors that want to invest with us, real estate sellers, buyers, and tenants who lease from us.

Our logo is attached

```html
<!DOCTYPE html>
<html lang="en">
<head>
<meta charset="utf-8">
<title>KORU Real Estate Holdings LLC — Business Cards</title>
<link href="https://fonts.googleapis.com/css2?family=Open+Sans:wght@400;600;700&display=swap" rel="stylesheet">
<style>
  :root {
    --stage: #8f8f8f;
    --card: #ffffff;
    --ink: #231f20;
    --text: #1a1a1a;
    --red: #d7262b;
    --divider: #e0272d;
  }
  * { box-sizing: border-box; margin: 0; padding: 0; }
  html, body {
    width: 1200px;
    height: 960px;
    overflow: hidden;
    background: var(--stage);
    font-family: "Open Sans", Arial, sans-serif;
  }
  .sheet {
    width: 1200px;
    height: 960px;
    display: flex;
    flex-direction: column;
    align-items: center;
    justify-content: center;
    gap: 34px;
  }
  .card {
    width: 760px;
    height: 434px;
    background: var(--card);
    position: relative;
    box-shadow: 0 4px 14px rgba(0,0,0,.25);
  }

  /* Wordmark lockup */
  .brand {
    display: flex;
    align-items: center;
    gap: 18px;
    color: var(--ink);
    font-weight: 700;
  }
  .brand__square {
    flex: none;
    background: var(--red);
  }
  .brand__text { display: flex; flex-direction: column; line-height: 1; }
  .brand__name { letter-spacing: .04em; }
  .brand__tagline { text-transform: uppercase; letter-spacing: .01em; margin-top: 10px; }

  /* Front */
  .card--front .brand {
    position: absolute;
    left: 110px;
    top: 50%;
    transform: translateY(-50%);
  }
  .card--front .brand__square { width: 70px; height: 70px; }
  .card--front .brand__name { font-size: 96px; }
  .card--front .brand__tagline { font-size: 24px; }

  /* Back */
  .card--back .brand {
    position: absolute;
    left: 46px;
    top: 50%;
    transform: translateY(-50%);
    gap: 12px;
  }
  .card--back .brand__square { width: 40px; height: 40px; }
  .card--back .brand__name { font-size: 56px; }
  .card--back .brand__tagline { font-size: 14px; margin-top: 6px; }

  .divider {
    position: absolute;
    left: 396px;
    top: 92px;
    width: 2px;
    height: 250px;
    background: linear-gradient(to bottom, transparent, var(--divider) 20%, var(--divider) 80%, transparent);
  }
  .contacts {
    position: absolute;
    left: 424px;
    top: 120px;
    list-style: none;
    display: flex;
    flex-direction: column;
    gap: 14px;
    font-size: 15px;
    color: var(--text);
  }
  .contacts li { display: flex; align-items: center; gap: 12px; }
  .contacts svg { width: 16px; height: 16px; flex: none; }
</style>
</head>
<body>
<main class="sheet">

  <section class="card card--front" aria-label="Business card front">
    <div class="brand">
      <span class="brand__square"></span>
      <div class="brand__text">
        <span class="brand__name">KORU</span>
        <span class="brand__tagline">Real Estate Holdings LLC</span>
      </div>
    </div>
  </section>

  <section class="card card--back" aria-label="Business card back">
    <div class="brand">
      <span class="brand__square"></span>
      <div class="brand__text">
        <span class="brand__name">KORU</span>
        <span class="brand__tagline">Real Estate Holdings LLC</span>
      </div>
    </div>

    <div class="divider"></div>

    <ul class="contacts">
      <li>
        <svg viewBox="0 0 16 16" aria-hidden="true"><rect x="4" y="1" width="8" height="14" rx="1.5" fill="var(--red)"/><rect x="5.5" y="3" width="5" height="8" fill="#fff"/></svg>
        <span>55 5555 5555</span>
      </li>
      <li>
        <svg viewBox="0 0 16 16" aria-hidden="true"><path d="M2 5c0-2 3-3 6-3s6 1 6 3v1h-3V5H5v1H2z" fill="var(--ink)"/><rect x="3" y="7" width="10" height="7" rx="1" fill="var(--ink)"/><circle cx="8" cy="10.5" r="1.6" fill="#fff"/></svg>
        <span>44 4444 4444</span>
      </li>
      <li>
        <svg viewBox="0 0 16 16" aria-hidden="true"><rect x="1" y="3.5" width="14" height="9" fill="var(--ink)"/><path d="M1.5 4l6.5 5 6.5-5" fill="none" stroke="#fff" stroke-width="1"/></svg>
        <span>info@korurealestate.com</span>
      </li>
      <li>
        <svg viewBox="0 0 16 16" aria-hidden="true" fill="none" stroke="var(--ink)" stroke-width="1.1"><circle cx="8" cy="8" r="6.5"/><ellipse cx="8" cy="8" rx="3" ry="6.5"/><path d="M1.5 8h13M2.5 4.8h11M2.5 11.2h11"/></svg>
        <span>www.korurealestate.com</span>
      </li>
      <li>
        <svg viewBox="0 0 16 16" aria-hidden="true"><path d="M8 1a4.5 4.5 0 0 0-4.5 4.5C3.5 9 8 15 8 15s4.5-6 4.5-9.5A4.5 4.5 0 0 0 8 1z" fill="var(--ink)"/><circle cx="8" cy="5.5" r="1.6" fill="var(--red)"/></svg>
        <span>area,state,zipcode,country</span>
      </li>
    </ul>
  </section>

</main>
</body>
</html>
```